Trade show booth design in Vector format.

Hello, I need a tradeshow booth design for a company called Valorine. I am in need of a background for a dental trade show I will be doing in 10 days. The format is 90" by 90" with a .25 bleed.

Here are my 2 websites with the products and services I offer, I think this can give you a good idea of the colors and styles of font we like.

www.clearvats.ca

http://valorine.example-sites.com

I'm thinking the type of theme of the background being the water theme I posted 1.1 MB file - with the phrase

"Des Solutions de traitement de l'eau efficaces et fiables pour votre clinique dentaire"

As the title text.

- with my 2 comapny logos integrated.

I am in need of this ASAP, so lets get going.

Raffaele

Target Market(s)

Dentists

Industry/Entity Type

Water Purification

Font styles to use
Sans Serif

Colors
33a6d7
85cae6
cee9f5
0692cd

Requirements
Must have
• My 2 logos - for my 2 companies.
• The slogan
• Des Solutions de traitement de l'eau efficaces et fiables pour votre clinique dentaire

```html
<!DOCTYPE html>
<html lang="fr">
<head>
<meta charset="utf-8">
<title>Valorine – Traitement de l'eau</title>
<link rel="stylesheet" href="https://fonts.googleapis.com/css2?family=Pathway+Gothic+One&family=Questrial&display=swap">
<style>
  :root {
    --paper: #ffffff;
    --ink: #4a86b0;
    --brand-teal: #7fbcc0;
    --water-light: #cee9f5;
    --water-mid: #5b93cf;
    --water-deep: #2c55a0;
  }
  html, body {
    margin: 0;
    padding: 0;
    width: 1200px;
    height: 1200px;
    overflow: hidden;
    background: var(--paper);
  }
  .booth {
    position: relative;
    width: 1200px;
    height: 1200px;
    background: var(--paper);
  }
  .brand-secondary {
    position: absolute;
    left: 160px;
    top: 214px;
    display: flex;
    align-items: center;
    gap: 14px;
    font-family: "Pathway Gothic One", sans-serif;
    font-size: 62px;
    letter-spacing: 1px;
    color: var(--brand-teal);
    line-height: 1;
  }
  .brand-secondary .dot {
    width: 22px;
    height: 22px;
    border-radius: 50%;
    background: var(--brand-teal);
  }
  .brand-primary {
    position: absolute;
    left: 686px;
    top: 196px;
    font-family: "Questrial", sans-serif;
    font-size: 104px;
    letter-spacing: 3px;
    color: var(--ink);
    line-height: 1;
  }
  .headline {
    position: absolute;
    left: 0;
    top: 438px;
    width: 1200px;
    margin: 0;
    text-align: center;
    font-family: "Pathway Gothic One", sans-serif;
    font-weight: 400;
    font-size: 60px;
    line-height: 72px;
    color: var(--ink);
  }
  .water {
    position: absolute;
    left: 0;
    top: 690px;
    width: 1200px;
    height: 510px;
    display: block;
  }
</style>
</head>
<body>
  <main class="booth">
    <div class="brand-secondary"><span class="dot"></span>CLEAR VATS</div>
    <div class="brand-primary">valorine</div>

    <h1 class="headline">Des Solutions de traitement de l'eau<br>efficaces et fiables pour votre<br>CLINIQUE DENTAIRE</h1>

    <svg class="water" viewBox="0 0 1200 510" role="img" aria-label="Illustration de surface d'eau bleue avec vague et bulles scintillantes">
      <defs>
        <linearGradient id="waterFill" x1="0" y1="0" x2="0" y2="1">
          <stop offset="0" stop-color="var(--water-deep)"/>
          <stop offset="0.55" stop-color="var(--water-mid)"/>
          <stop offset="1" stop-color="#6fa4da"/>
        </linearGradient>
        <linearGradient id="foamFill" x1="0" y1="0" x2="0" y2="1">
          <stop offset="0" stop-color="#ffffff"/>
          <stop offset="1" stop-color="var(--water-light)"/>
        </linearGradient>
      </defs>
      <path d="M0 30 C 200 10, 420 60, 600 80 C 800 100, 1000 60, 1200 10 L1200 510 L0 510 Z" fill="url(#foamFill)"/>
      <path d="M0 90 C 180 130, 380 120, 560 100 C 700 90, 800 150, 840 110 C 900 60, 1000 80, 1200 86 L1200 510 L0 510 Z" fill="url(#waterFill)"/>
    </svg>
  </main>
</body>
</html>
```